Varlan, Dobre and Associates (Corporate Identity)

We need a corporate identity design (logo, business card, letter, email signature and power point template) for a new lawyers company named: Varlan, Dobre and Associates.
The company has as main objective to provide the most suitable legal solutions to his partners. We want to position ourselves as a young and dynamic company with an ambitious team of lawyers and professionals.
We want a logo that uses a simple and clear legible font so that it can be used on any media (print , web or video). We want colors to express the dynamic, youthful but also and seriousness and professionalism.
The final design should communicate reliability, trust and professionalism.

Industry/Entity Type

Business

Logo Text

Varlan, Dobre and Associates

Requirements
Must have
• For those who design the logo only with accent on "Varlan" pease be informed that the both two names are important (Varlan and Dobre). Both are the main partners of the company, "Associates" are secondary. Please adjusr your designs.
• please take into consideration that we need also and the design for letter and email signature. Please complete the business card design with a fictive contacts, to see the complete design. Thank you!

```html
<!DOCTYPE html>
<html lang="en">
<head>
<meta charset="utf-8">
<title>Varlan, Dobre and Associates – Stationery</title>
<link href="https://fonts.googleapis.com/css2?family=Questrial&family=Arimo:wght@400&display=swap" rel="stylesheet">
<style>
  :root {
    --teal: #14a89a;
    --ink: #2b2b2b;
    --grey: #6e6e6e;
    --paper: #ffffff;
    --backdrop: #f2f2f0;
    --edge: #dedede;
  }
  * { margin: 0; padding: 0; box-sizing: border-box; }
  html, body { width: 1200px; height: 1000px; overflow: hidden; }
  body {
    position: relative;
    background: var(--backdrop);
    font-family: "Arimo", Arial, sans-serif;
  }
  .sheet {
    position: absolute;
    background: var(--paper);
    border: 1px solid var(--edge);
  }
  .letterhead { left: 74px; top: 52px; width: 635px; height: 896px; }
  .business-card { left: 784px; top: 92px; width: 338px; height: 205px; }
  .envelope { left: 491px; top: 351px; width: 635px; height: 297px; }

  .wordmark {
    position: absolute;
    font-family: "Questrial", sans-serif;
    color: var(--teal);
    line-height: 1;
    white-space: nowrap;
  }
  .wordmark .partners, .wordmark .associates { display: block; }
  .wordmark.centered { text-align: center; transform: translateX(-50%); }

  .letterhead .wordmark { left: 317px; top: 120px; }
  .letterhead .partners { font-size: 30px; }
  .letterhead .associates { font-size: 18px; margin-top: 2px; }

  .business-card .wordmark { left: 169px; top: 48px; }
  .business-card .partners { font-size: 20px; }
  .business-card .associates { font-size: 13px; margin-top: 1px; }

  .envelope .wordmark { left: 38px; top: 55px; }
  .envelope .partners { font-size: 23px; }
  .envelope .associates { font-size: 14px; margin-top: 1px; padding-left: 32px; }

  .standalone-mark .wordmark { left: 923px; top: 776px; }
  .standalone-mark .partners { font-size: 31px; }
  .standalone-mark .associates { font-size: 20px; margin-top: 2px; }

  .contact {
    position: absolute;
    color: var(--grey);
    line-height: 1;
    white-space: nowrap;
  }
  .contact.centered { text-align: center; transform: translateX(-50%); }

  .letter-footer { left: 317px; top: 838px; font-size: 10px; }
  .letter-footer p + p { margin-top: 8px; }

  .card-person { position: absolute; left: 169px; top: 114px; transform: translateX(-50%); text-align: center; line-height: 1; }
  .card-person .name { font-size: 12px; color: var(--ink); }
  .card-person .role { font-size: 8px; color: var(--grey); margin-top: 3px; }
  .card-footer { left: 169px; top: 166px; font-size: 8px; }
  .card-footer p + p { margin-top: 5px; }

  .envelope-return { left: 44px; top: 204px; font-size: 9px; }
  .envelope-return p + p { margin-top: 9px; }

  .mark-contacts { left: 923px; top: 853px; font-size: 12px; }
  .mark-contacts p + p { margin-top: 4px; }
</style>
</head>
<body>
  <section class="sheet letterhead" aria-label="Letterhead">
    <div class="wordmark centered">
      <span class="partners">Varlan Dobre</span>
      <span class="associates">and Associates</span>
    </div>
    <div class="contact centered letter-footer">
      <p>Building North Avenue 52 | Tel +1098765432 Fax +1098765432</p>
      <p>lawyer@varlandobre.com | www.varlandobre.com</p>
    </div>
  </section>

  <section class="sheet business-card" aria-label="Business card">
    <div class="wordmark centered">
      <span class="partners">Varlan Dobre</span>
      <span class="associates">and Associates</span>
    </div>
    <div class="card-person">
      <p class="name">Andrei Popa</p>
      <p class="role">Lawyer</p>
    </div>
    <div class="contact centered card-footer">
      <p>Building North Avenue 52 | Tel +1098765432 Fax +1098765432</p>
      <p>lawyer@varlandobre.com | www.varlandobre.com</p>
    </div>
  </section>

  <section class="sheet envelope" aria-label="Envelope">
    <div class="wordmark">
      <span class="partners">Varlan Dobre</span>
      <span class="associates">and Associates</span>
    </div>
    <div class="contact envelope-return">
      <p>Building North Avenue 52</p>
      <p>Tel +1098765432 Fax +1098765432</p>
      <p>lawyer@varlandobre.com</p>
      <p>www.varlandobre.com</p>
    </div>
  </section>

  <section class="standalone-mark" aria-label="Email signature">
    <div class="wordmark centered">
      <span class="partners">Varlan Dobre</span>
      <span class="associates">and Associates</span>
    </div>
    <div class="contact centered mark-contacts">
      <p>Tel +12 987 65430 &nbsp; Fax +12 987 65430</p>
      <p>Email law@varlandobre.com</p>
    </div>
  </section>
</body>
</html>
```